2nd Opinion Radiology web page

Looking for a web page design for second opinion radiology service. Main page will have a link directing user to locate CD on their computer/device, and will take contents of CD and upload to server, which I will specify.

Web page needs a form to enter user's name, contact info, and create a log in for user. User must click to accept terms of service, which will be a paragraph which i will provide. User will log back in, after uploading cd, to find report, which will be able to be viewed once user pays, by zumbit. User will need to be able to download report.

There will be a small paragraph explaining what we do: Provide expert second opinions, worldwide. We provide interpretations from radiologists with many years of experience and training from the world's best institutions, including corwent and halvering general hospital.

A second paragraph: Have questions or doubts about your CT or MRI? Get a second opinion from experts at Vexorly. Tap into the full potential of your images.

Thanks
Updates

Reason: The website does not need to be fully coded, however, should include graphics and design so a web designer can simply take the design, images, and objects and code the site.

Target Market(s)

People who are unsure of their medical care and looking for a second opinion.

Industry/Entity Type

Training

Files

```html
<!DOCTYPE html>
<html lang="en">
<head>
<meta charset="utf-8">
<title>Vexorly – Report</title>
<link href="https://fonts.googleapis.com/css2?family=Didact+Gothic&display=swap" rel="stylesheet">
<style>
  :root {
    --ink: #2b2b2b;
    --ink-soft: #555;
    --paper: #ffffff;
    --header-dark: #07121c;
    --header-teal: #2f6e74;
    --brand: #5f86c4;
    --link: #1a1ae6;
    --rail: #000000;
  }
  * { margin: 0; padding: 0; box-sizing: border-box; }
  html, body { width: 1062px; height: 1200px; overflow: hidden; background: var(--paper); }
  body { position: relative; font-family: "Didact Gothic", "Century Gothic", sans-serif; color: var(--ink); }

  .rail-shadow {
    position: absolute; left: 120px; top: 178px; width: 92px; height: 1022px;
    background: linear-gradient(to right, rgba(255,255,255,0), rgba(0,0,0,0.35));
  }
  .rail {
    position: absolute; left: 204px; top: 0; width: 11px; height: 1200px;
    background: linear-gradient(to right, #222, var(--rail) 40%, #333);
    border-radius: 5px;
  }

  .site-header {
    position: absolute; left: 38px; top: 25px; width: 743px; height: 127px;
    background: linear-gradient(100deg, var(--header-dark) 0%, #0b2636 45%, var(--header-teal) 75%, #1f4f56 100%);
    border-top: 2px solid #0d2a55;
  }
  .brand-name {
    position: absolute; left: 60px; top: 32px;
    font-size: 46px; color: var(--brand); letter-spacing: 1px; line-height: 1;
  }
  .brand-tagline {
    position: absolute; left: 82px; top: 80px;
    font-size: 16px; color: #e8eef4;
  }
  .header-art {
    position: absolute; right: 28px; top: 12px; width: 230px; height: 105px;
    background: radial-gradient(ellipse at center, #e8f2f2 0%, #6fa4a8 25%, rgba(47,110,116,0.4) 60%, rgba(47,110,116,0) 100%);
  }

  .top-nav {
    position: absolute; left: 272px; top: 160px; width: 500px;
    font-size: 10px; color: var(--ink-soft);
  }
  .top-nav span { position: absolute; top: 0; white-space: nowrap; }
  .top-nav .user { color: #000; }

  .print-link { position: absolute; left: 564px; top: 188px; font-size: 12.5px; color: var(--link); text-decoration: underline; }

  .report { position: absolute; left: 235px; top: 206px; width: 400px; font-size: 12.5px; line-height: 14.7px; }
  .report h2 { font-size: 11.5px; font-weight: bold; font-family: Arial, sans-serif; margin-top: 14px; }
  .scan {
    position: absolute; left: 235px; top: 377px; width: 191px; height: 177px;
    background: radial-gradient(ellipse at 50% 50%, #3b8fb0 0%, #1c5a78 45%, #081d2a 80%);
  }
  .overview-text { position: absolute; left: 235px; top: 572px; width: 390px; font-size: 12.5px; line-height: 15.2px; }

  .backdrop-figure {
    position: absolute; left: 549px; top: 398px; width: 513px; height: 584px;
    background: radial-gradient(ellipse at 65% 40%, #e2e2e2 0%, #ececec 40%, rgba(255,255,255,0) 72%);
  }
</style>
</head>
<body>
  <div class="rail-shadow"></div>
  <div class="rail"></div>

  <header class="site-header">
    <div class="brand-name">vexorly.co</div>
    <div class="brand-tagline">Global Expert Second Opinions</div>
    <div class="header-art" role="img" aria-label="CT and MRI illustration of two facing head profiles"></div>
  </header>

  <nav class="top-nav">
    <span style="left:0">Send Request</span>
    <span style="left:80px">|</span>
    <span style="left:101px">Locate CD</span>
    <span style="left:163px">|</span>
    <span style="left:178px">Login</span>
    <span style="left:216px">|</span>
    <span style="left:231px">Contact</span>
    <span class="user" style="left:351px">TEST, Customer</span>
    <span style="left:434px">Logged In</span>
  </nav>

  <div class="backdrop-figure" role="img" aria-label="Faint illustration of a head profile with brain"></div>

  <a class="print-link" href="#">Print</a>

  <section class="report">
    <p>Name: Customer TEST</p>
    <p>Date of Birth: 29 / 06 / 1986</p>
    <p>Scan Date: 01 / 01 / 2014</p>
    <p>Radiologist: Dr Alan Pemberley</p>
    <p>Overview Completed: 01/02/2014</p>
    <p>Request for Interpretation: Azygoesophageal Recess</p>
    <h2>RESULT:</h2>
    <p>Major Abnormaility</p>
    <h2>Overview:</h2>
  </section>

  <div class="scan" role="img" aria-label="Axial chest CT scan with arrows marking a mass"></div>

  <p class="overview-text">Morphologic criteria on thin-section CT scans include bronchial dilatation with respect to the accompanying pulmonary artery (signet ring sign), lack of tapering of bronchi, and identification of bronchi within 1 cm of the pleural surface (27) (Fig 11). Bronchiectasis may be classified as cylindric, varicose, or cystic, depending on the appearance of the affected bronchi. It is often accompanied by bronchial wall thickening, mucoid impaction, and small-airways abnormalities (27–29). (See also signet ring sign.)</p>
</body>
</html>
```